New Toothpaste brand needs a logo & packaging design

Our company is launching a new toothpaste and is looking for a logo and packaging design. The toothpaste brand is called Brivana. The packaging should have the same design quality as the major international brands, such as Lumora, Lumora Totalcare, Dentiva, Pexolo, Wind-rise, Marvest, etc. The dominant colors for our brand should be hues of blue, similar to other major brands. In addition, there should be a little bit of green to represent the "Fresh Mint Blast" flavor and the "Extracts of Aloe Vera" included in the ingredients.

There are typically 3 unique sides on a toothpaste box:

The face: Repeated on ~3 sides of the 4 faces of the box
The back: The 4th box face has the instructions for use, ingredients, company information, bar code/product info, and some branding elements.
The sides: Usually consisting of just the logo, flavor etc.

Please refer to existing brands such as Lumora, Lumora Total-care, and Dentiva for an example of typical box layout and elements.

Task Details:
Package Dimensions: 180 mm x 48 mm x 28 mm, 100 ml toothpaste tube
Brand Name: Brivana
Description: Fluoride Toothpaste
Flavor: Fresh Mint Blast
5 Actions: Protects against cavities and tartar, freshens breath, whitens teeth, and maintains healthy gums. These actions can also be made into a list like Lumora Total Care or Dentiva Max care. For instance, Strong Teeth, Fresh Breath, Whitening, Healthy Gums, Cavity and Tartar Protection.
Also contains whitening micro particles and extracts of aloe vera which may be highlighted on the package

Overall, the look should be high quality and with the same look and feel as the big brands mentioned previously. We do not have an existing logo for this brand. The face of the package is the most important element as it is often repeated on several sides and on the tube itself.

Please let me know if you have any questions.

I've attached some of our favorite big brand designs below. I would say the Lumora Total Care and Gleam vers

The logos I've seen so far for Brivana, have been a bit too bold. A little bold is okay, but just needs to be moderate. 

I would like the colors to be bright and appealing. I mentioned shades of blue being the major color, but green should also be highlighted as well, perhaps in a 80% blue to 20% green ratio. 

Target Market(s)

adult consumer of toothpaste, both female and male.

Industry/Entity Type

It Company

Requirements
Must have
• A logo with the brand name: Brivana
Description or sub text: Fluoride Toothpaste
Flavor: Fresh Mint Blast
A phrase or list describing the Toothpaste Actions: e.g., Protects against cavities and tartar, freshens breath, whitens teeth, and maintains healthy gums. Or as a list simialr to Lumora Total Care or Dentiva Max Care:
-Anti-cavity
-Anti-tartar
-Fresh breath
-Whitening
-Healthy Gums

Special ingredient of "whitening micro particles: and "extracts of aloe vera", which should also be highlighted.

The color should mostly be shades of blue, with only a little bit of green to accentuate the fresh mint blast flavor and aloe vera

Nice to have
• The design should really look good next to lumora total care, gleam pure, and dentiva max care. These are our favorite designs.
Should not have
• For aloe vera, there is no need to show the plant.

The Brivana logo shouldn't be too Bold. This should be appeal to all consumers, not just men.

```html
<!DOCTYPE html>
<html lang="en">
<head>
<meta charset="utf-8">
<title>Brivana Fluoride Toothpaste – Box Face</title>
<link href="https://fonts.googleapis.com/css2?family=Arimo:ital,wght@0,400;0,700;1,400;1,700&display=swap" rel="stylesheet">
<style>
  :root {
    --page-bg: #f2f2f2;
    --navy: #163f8f;
    --navy-deep: #0f2f73;
    --blue-mid: #0a7fcf;
    --blue-bright: #0fb1ec;
    --glow: #ffffff;
    --green-light: #a3cf3b;
    --green: #3bb54a;
    --white: #ffffff;
  }
  * { margin: 0; padding: 0; box-sizing: border-box; }
  html, body {
    width: 1200px;
    height: 900px;
    overflow: hidden;
    background: var(--page-bg);
    font-family: "Arimo", Arial, sans-serif;
  }
  .box-face {
    position: absolute;
    left: 208px;
    top: 271px;
    width: 789px;
    height: 211px;
    overflow: hidden;
    background:
      radial-gradient(ellipse 260px 110px at 330px 105px, rgba(255,255,255,0.55), rgba(255,255,255,0) 70%),
      linear-gradient(90deg, rgba(12,40,110,0) 70%, rgba(12,40,110,0.45) 100%),
      linear-gradient(180deg,
        var(--navy) 0%,
        var(--blue-mid) 28%,
        var(--blue-bright) 42%,
        #bfeefd 48.5%,
        var(--glow) 50%,
        #bfeefd 51.5%,
        var(--blue-bright) 58%,
        var(--blue-mid) 78%,
        var(--navy-deep) 100%);
  }
  .new-corner {
    position: absolute;
    left: 0;
    top: 0;
    width: 72px;
    height: 72px;
    background: var(--white);
    clip-path: polygon(0 0, 100% 0, 0 100%);
  }
  .new-corner__label {
    position: absolute;
    left: 6px;
    top: 14px;
    transform: rotate(-45deg);
    font-weight: 700;
    font-style: italic;
    font-size: 12px;
    color: var(--navy);
    letter-spacing: 0.5px;
  }
  .brand {
    position: absolute;
    left: 76px;
    top: 64px;
  }
  .brand__name {
    display: block;
    font-weight: 700;
    font-size: 64px;
    line-height: 1;
    color: var(--navy);
    letter-spacing: -0.5px;
  }
  .brand__descriptor {
    display: block;
    margin: 4px 0 0 70px;
    font-weight: 700;
    font-style: italic;
    font-size: 13.5px;
    color: var(--navy-deep);
  }
  .actions-tab {
    position: absolute;
    left: 582px;
    top: -4px;
    width: 131px;
    height: 160px;
    border: 3px solid var(--white);
    border-radius: 0 0 28px 28px;
    background: linear-gradient(180deg, var(--green-light) 0%, var(--green) 65%);
    display: flex;
    flex-direction: column;
    align-items: center;
    padding-top: 31px;
    list-style: none;
  }
  .actions-tab li {
    font-weight: 700;
    font-size: 12.5px;
    line-height: 20px;
    letter-spacing: 0.9px;
    color: var(--white);
  }
  .flavor-pill {
    position: absolute;
    left: 0;
    top: 171px;
    width: 144px;
    height: 31px;
    border-radius: 0 16px 16px 0;
    background: linear-gradient(90deg, var(--green) 0%, var(--green-light) 100%);
    display: flex;
    align-items: center;
    padding-left: 11px;
    gap: 10px;
  }
  .flavor-pill__text {
    font-weight: 700;
    font-size: 9.5px;
    color: var(--white);
  }
  .flavor-pill__icon { width: 24px; height: 12px; }
  .ingredient-line {
    position: absolute;
    left: 156px;
    top: 180px;
    font-size: 12.5px;
    color: var(--white);
  }
  .ingredient-line strong { font-style: italic; font-weight: 700; }
</style>
</head>
<body>
  <section class="box-face" aria-label="Brivana toothpaste box face">
    <div class="new-corner"><span class="new-corner__label">NEW</span></div>

    <div class="brand">
      <span class="brand__name">Brivana</span>
      <span class="brand__descriptor">Fluoride Toothpaste</span>
    </div>

    <ul class="actions-tab">
      <li>Anti-cavity</li>
      <li>Anti-tartar</li>
      <li>Fresh Breath</li>
      <li>Whitening</li>
      <li>Healthy Gums</li>
    </ul>

    <div class="flavor-pill">
      <span class="flavor-pill__text">Fresh Mint Blast</span>
      <svg class="flavor-pill__icon" viewBox="0 0 24 12" aria-hidden="true">
        <path d="M2 7 C4 2, 12 1, 22 3 C23 6, 20 10, 12 10 C7 10, 3 9, 2 7 Z" fill="#ffffff" stroke="#9fb6c8" stroke-width="0.8"/>
      </svg>
    </div>

    <p class="ingredient-line">Special ingredient of <strong>Whitening Micro Particles</strong> and <strong>Extracts Of Aloe Vera</strong></p>
  </section>
</body>
</html>
```